Market online tutoring + Back to School + give Support for students school work K to 12 Grade

To promote my tutoring business online need to create a two sided flyer. Need to get the attention of parents and educators who looking for help to support the digital learning of their students due to COVID-19 lock down. I need to project and differentiate that we offer support for online school with individualized learning . We tutor Elementary to High school students on all subjects you may take a look at my website brightpinetutors.com for additional info and also I can provide
Updates

Hi All Due to Covid, we were unable to work on this project on time as originally planned. We were given an extension until March 15 and we will complete it by then. Sorry for any inconvenience and Thank you for your support. -Wren Institute

Target Market(s)

Parents and students

Industry/Entity Type

Education

Requirements
Must have
• For online less fine print on the first page. The phone number and support text message. Back to School , Support Online learning SAT/ACT test prep should have some focus
Nice to have
• Discuss the platform We created a platform with live instructor interaction, virtual classroom, instructional videos, assessments, and practice to support every individual student’s need. We are confident in our ability to provide the most effective distance learning experience.
Should not have
• too much clunky and packed with content. Should be easy to read with color

```html
<!DOCTYPE html>
<html lang="en">
<head>
<meta charset="utf-8">
<title>Wren Institute – Two-Sided Flyer</title>
<link href="https://fonts.googleapis.com/css2?family=Oswald:wght@400;500;600&family=Montserrat:wght@400;500;600;700&family=Roboto+Slab:wght@400;500;700&family=Patrick+Hand&display=swap" rel="stylesheet">
<style>
:root{
  --red:#d0222a;
  --red-dark:#a8141c;
  --navy:#0f3a4c;
  --navy-deep:#0b2f3e;
  --beige:#ead7bd;
  --beige-light:#f2e4cf;
  --pill:#262626;
  --white:#ffffff;
  --grey-text:#5b5b5b;
  --canvas:#e4e4e2;
}
*{box-sizing:border-box;margin:0;padding:0}
html,body{width:1200px;height:973px;overflow:hidden}
body{background:var(--canvas);font-family:"Montserrat",sans-serif;position:relative}
.flyer{position:absolute;top:133px;width:501px;height:707px;overflow:hidden;box-shadow:0 2px 8px rgba(0,0,0,.18)}
.flyer--front{left:82px;background:var(--red)}
.flyer--back{left:617px;background:var(--navy)}
.abs{position:absolute}

/* front */
.front-photo{left:0;top:0;width:501px;height:310px;background:linear-gradient(135deg,var(--beige-light),var(--beige) 60%,#dcc4a4)}
.headline{left:30px;top:30px}
.headline .prep{font-family:"Roboto Slab",serif;font-weight:700;font-size:32px;color:var(--navy);line-height:1;white-space:nowrap}
.headline .big{font-family:"Roboto Slab",serif;font-weight:500;font-size:37px;color:var(--red-dark);line-height:1.02;margin-top:6px}
.headline .mid{font-family:"Roboto Slab",serif;font-weight:500;font-size:28px;color:var(--navy);line-height:1.1;white-space:nowrap}
.laptop-icon{left:30px;top:212px}
.brand{left:0;width:501px;top:254px;display:flex;align-items:center;justify-content:center;gap:8px}
.brand .dot{width:14px;height:14px;border-radius:50%;background:var(--white)}
.brand .name{font-weight:700;font-size:18px;color:var(--white);letter-spacing:1px}
.platform-title{left:0;width:501px;top:346px;text-align:center;font-weight:600;font-size:17px;color:#f7d9c9}
.feature{height:37px;background:var(--pill);border-radius:4px;display:flex;align-items:center;gap:7px;padding:0 7px;color:var(--white);font-size:13px;line-height:1;white-space:nowrap}
.feature svg{flex:none}
.confidence{left:0;width:501px;top:480px;text-align:center;color:#f4d8cf;font-size:14.5px;line-height:1.05}
.home-panel{left:24px;top:533px;width:457px;height:94px;background:linear-gradient(#ffffff,#d9d9d9);border-radius:3px;padding:9px 13px;white-space:nowrap}
.home-panel .h1{font-family:"Oswald",sans-serif;font-weight:600;font-size:30px;color:var(--red);line-height:1}
.home-panel .h2{font-family:"Patrick Hand",cursive;font-size:27px;color:var(--navy);line-height:1.1}
.home-panel .h3{font-style:italic;font-size:12.5px;color:var(--grey-text);letter-spacing:.3px;line-height:1}
.contact{left:25px;top:645px;width:451px;height:41px;border-radius:21px;display:flex;align-items:center;justify-content:center;gap:12px;font-family:"Oswald",sans-serif;font-weight:500;font-size:19px;color:var(--white);white-space:nowrap;line-height:1}
.contact b{color:var(--red);font-weight:500}
.contact--dark{background:linear-gradient(#333,#1b1b1b);border:2px solid #4a0d10}
.contact--red{background:linear-gradient(#e02a31,#b3161d);border:2px solid #7f1015}
.contact--red b{color:var(--navy-deep)}

/* back */
.back-photo{left:0;top:0;width:501px;height:212px;background:linear-gradient(180deg,#f3efe8,#e5ddd1)}
.section-title{left:0;width:501px;display:flex;align-items:center;justify-content:center;gap:6px;color:var(--white);font-weight:700;white-space:nowrap}
.section-title::before,.section-title::after{content:"";height:1px;background:var(--white);width:52px}
.why{top:171px;font-size:19px}
.courses{top:432px;font-size:21px}
.courses::before,.courses::after{width:56px}
.reason{width:225px;display:flex;gap:9px}
.reason .icon{flex:none;width:58px;height:54px;background:var(--red);border-radius:6px;display:flex;align-items:center;justify-content:center}
.reason h3{font-family:"Oswald",sans-serif;font-weight:500;font-size:15px;color:#ff3b3f;line-height:1;text-transform:uppercase;white-space:nowrap}
.reason p{font-size:8.2px;line-height:1.2;color:var(--white);margin-top:3px}
.plan{top:470px;width:130px;height:142px;background:linear-gradient(#fafafa,#dedede)}
.plan .head{height:33px;background:var(--red);color:var(--white);font-family:"Oswald",sans-serif;font-weight:500;font-size:14px;display:flex;align-items:center;justify-content:center}
.plan ul{list-style:none;text-align:center;font-size:8.4px;color:var(--grey-text);line-height:15px;margin-top:7px;white-space:nowrap}
.plan ul li:first-child{color:var(--red);font-weight:600}
.plan .price{position:absolute;left:28px;top:122px;width:74px;height:29px;background:var(--red);border:2px solid var(--navy-deep);border-radius:7px;color:var(--white);font-weight:600;font-size:18px;display:flex;align-items:center;justify-content:center}
</style>
</head>
<body>

<!-- FRONT -->
<section class="flyer flyer--front">
  <div class="abs front-photo" role="img" aria-label="Photo of two smiling children with school backpacks flying across a beige floor with a soccer ball and an open book"></div>
  <svg class="abs" style="left:0;top:0" width="501" height="707" viewBox="0 0 501 707">
    <polygon points="0,310 248,206 501,310 501,707 0,707" fill="var(--navy)"/>
    <polygon points="0,322 248,220 501,322 501,707 0,707" fill="var(--red)"/>
  </svg>

  <div class="abs headline">
    <div class="prep">TEST PREP</div>
    <div class="big">LEARN</div>
    <div class="mid">ANY WHERE</div>
    <div class="big" style="margin-top:0">LEARN</div>
    <div class="mid">ONLINE</div>
  </div>
  <svg class="abs laptop-icon" width="48" height="36" viewBox="0 0 48 36" fill="none" stroke="#d8b770" stroke-width="2.5">
    <rect x="7" y="3" width="34" height="23" rx="1"/>
    <path d="M3 31h42" stroke-width="4"/>
    <path d="M18 11l8 4-3 1 3 4-2 1-3-4-2 2z" fill="#d8b770" stroke="none"/>
  </svg>

  <div class="abs brand"><span class="dot"></span><span class="name">WREN INSTITUTE</span></div>

  <div class="abs platform-title">WE CREATED A PLATFORM WITH</div>

  <div class="abs feature" style="left:34px;top:378px;width:151px">
    <svg width="26" height="22" viewBox="0 0 30 22"><rect x="2" y="1" width="26" height="16" fill="var(--red)"/><circle cx="15" cy="7" r="3" fill="#fff"/><path d="M10 15c0-3 10-3 10 0z" fill="#fff"/><rect x="0" y="18" width="30" height="3" fill="var(--red)"/></svg>
    <span>Live instructor<br>Interaction</span>
  </div>
  <div class="abs feature" style="left:192px;top:378px;width:129px">
    <svg width="26" height="24" viewBox="0 0 30 24"><path d="M2 3h11v19H2zM15 3h13v19H15z" fill="none" stroke="var(--red)" stroke-width="2.5"/><path d="M19 9l6 3-6 3z" fill="var(--red)"/></svg>
    <span>Virtual<br>Classroom</span>
  </div>
  <div class="abs feature" style="left:327px;top:378px;width:143px">
    <svg width="26" height="26" viewBox="0 0 30 26"><rect x="3" y="1" width="24" height="24" fill="none" stroke="var(--red)" stroke-width="2.5"/><path d="M7 8h4M14 8h9M7 14h4M14 14h9M7 20h4M14 20h9" stroke="var(--red)" stroke-width="2.5"/></svg>
    <span>Assessments<br>&amp; Practice</span>
  </div>
  <div class="abs feature" style="left:71px;top:428px;width:213px">
    <svg width="26" height="30" viewBox="0 0 30 30"><path d="M5 7l10-4 10 4-10 4z" fill="var(--red)"/><circle cx="15" cy="14" r="5" fill="var(--red)"/><path d="M5 29c0-8 20-8 20 0z" fill="var(--red)"/></svg>
    <span>Support every Individual<br>Student’s need.</span>
  </div>
  <div class="abs feature" style="left:294px;top:428px;width:136px">
    <svg width="26" height="28" viewBox="0 0 30 28"><rect x="2" y="2" width="20" height="20" fill="none" stroke="var(--red)" stroke-width="2.5"/><path d="M6 8h10M6 13h10" stroke="var(--red)" stroke-width="2.5"/><circle cx="21" cy="20" r="7" fill="#fff"/><path d="M19 16l6 4-6 4z" fill="var(--red)"/></svg>
    <span>Instructional<br>Videos</span>
  </div>

  <div class="abs confidence">We are confident in our ability to provide<br>the most effective distance learning experience.</div>

  <div class="abs home-panel">
    <div class="h1">CONTINUE LEARNING FROM HOME</div>
    <div class="h2">Digital learning during COVID-19 lockdown</div>
    <div class="h3">We tutor Elementary to High school students on all subjects</div>
  </div>

  <div class="abs contact contact--dark"><span><b>CALL US :</b> 555-214-7730</span><span><b>VISIT US :</b> BRIGHTPINETUTORS.COM</span></div>
</section>

<!-- BACK -->
<section class="flyer flyer--back">
  <div class="abs back-photo" role="img" aria-label="Photo of two young children using laptops in a bright classroom with colourful shelves"></div>
  <svg class="abs" style="left:0;top:0" width="501" height="260" viewBox="0 0 501 260">
    <polygon points="0,207 250,100 501,207 501,260 0,260" fill="var(--red)"/>
    <polygon points="0,219 250,112 501,219 501,260 0,260" fill="var(--navy)"/>
  </svg>

  <div class="abs section-title why">WHY US</div>

  <div class="abs reason" style="left:25px;top:218px">
    <div class="icon"><svg width="30" height="30" viewBox="0 0 30 30" fill="none" stroke="#fff" stroke-width="2.5"><path d="M5 17v-3a10 10 0 0 1 20 0v3"/><rect x="3" y="16" width="5" height="8" rx="2" fill="#fff"/><rect x="22" y="16" width="5" height="8" rx="2" fill="#fff"/><path d="M24 24c0 3-4 4-8 4"/></svg></div>
    <div><h3>Support</h3><p>Lorem ipsum dolor sit amet consectetur adipiscing elit, sed do eiusmod tempor incididunt ut labore et dolore magna aliqua.</p></div>
  </div>
  <div class="abs reason" style="left:256px;top:218px">
    <div class="icon"><svg width="30" height="30" viewBox="0 0 30 30" fill="none" stroke="#fff" stroke-width="2.5"><path d="M5 2h14l5 5v19H5z"/><path d="M9 12h10M9 17h7"/><circle cx="22" cy="23" r="5" fill="#fff"/><path d="M19.5 23l2 2 3-4" stroke="var(--red)" stroke-width="2"/></svg></div>
    <div><h3>Effective Curriculum</h3><p>Lorem ipsum dolor sit amet consectetur adipiscing elit, sed do eiusmod tempor incididunt ut labore et dolore magna aliqua.</p></div>
  </div>
  <div class="abs reason" style="left:25px;top:285px">
    <div class="icon"><svg width="30" height="30" viewBox="0 0 30 30" fill="none" stroke="#fff" stroke-width="2.5"><rect x="12" y="4" width="15" height="11"/><circle cx="6" cy="7" r="3" fill="#fff"/><path d="M6 11v16M3 14h9M4 27l2-7 2 7M20 15l-3 10M20 15l3 10"/></svg></div>
    <div><h3>Awesome Teachers</h3><p>Lorem ipsum dolor sit amet consectetur adipiscing elit, sed do eiusmod tempor incididunt ut labore et dolore magna aliqua.</p></div>
  </div>
  <div class="abs reason" style="left:256px;top:285px">
    <div class="icon"><svg width="30" height="30" viewBox="0 0 30 30"><path d="M9 13V8a6 6 0 0 1 12 0" fill="none" stroke="#fff" stroke-width="2.5"/><rect x="6" y="13" width="18" height="14" rx="2" fill="#fff"/><circle cx="15" cy="19" r="2" fill="var(--red)"/><path d="M14 20h2v4h-2z" fill="var(--red)"/></svg></div>
    <div><h3>Unlimited Access</h3><p>Lorem ipsum dolor sit amet consectetur adipiscing elit, sed do eiusmod tempor incididunt ut labore et dolore magna aliqua.</p></div>
  </div>
  <div class="abs reason" style="left:25px;top:352px">
    <div class="icon"><svg width="30" height="30" viewBox="0 0 30 30"><path d="M3 14V4h10l14 14-10 10z" fill="#fff"/><circle cx="8" cy="9" r="2" fill="var(--red)"/></svg></div>
    <div><h3>Easy Pricing</h3><p>Lorem ipsum dolor sit amet consectetur adipiscing elit, sed do eiusmod tempor incididunt ut labore et dolore magna aliqua.</p></div>
  </div>
  <div class="abs reason" style="left:256px;top:352px">
    <div class="icon"><svg width="32" height="32" viewBox="0 0 32 32" fill="none" stroke="#fff" stroke-width="2.2"><rect x="4" y="3" width="24" height="17"/><path d="M9 7l7 2 7-2v9l-7 2-7-2zM16 9v9M2 22h28"/><path d="M10 27c2-3 4-3 6 0s4 3 6 0-4-3-6 0-4 3-6 0z"/></svg></div>
    <div><h3>Unlimited Online Practice</h3><p>Lorem ipsum dolor sit amet consectetur adipiscing elit, sed do eiusmod tempor incididunt ut labore et dolore magna aliqua.</p></div>
  </div>

  <div class="abs section-title courses">AVAILABLE COURSES</div>

  <div class="abs plan" style="left:26px">
    <div class="head">STARTER</div>
    <ul><li>Monthly Plan &nbsp;$100</li><li>Unlimited Course Access</li><li>Unlimited online Practice</li><li>24x7 support</li><li>Certification</li></ul>
    <div class="price">$100</div>
  </div>
  <div class="abs plan" style="left:186px">
    <div class="head">MEDIUM</div>
    <ul><li>Monthly Plan &nbsp;$200</li><li>Unlimited Course Access</li><li>Unlimited online Practice</li><li>24x7 support</li><li>Certification</li></ul>
    <div class="price">$200</div>
  </div>
  <div class="abs plan" style="left:340px">
    <div class="head">PREMIUM</div>
    <ul><li>Monthly Plan &nbsp;$300</li><li>Unlimited Course Access</li><li>Unlimited online Practice</li><li>24x7 support</li><li>Certification</li></ul>
    <div class="price">$300</div>
  </div>

  <div class="abs contact contact--red"><span><b>CALL US :</b> 555-214-7730</span><span><b>VISIT US :</b> BRIGHTPINETUTORS.COM</span></div>
</section>

</body>
</html>
```